Redesign of existing website for a corporate advisory business focussed on technology

We need a redesign of our website. We are a corporate advisory business based in Sydney. Our focus is on the technology and life-science sectors. We assist our clients with capital raisings, mergers and acquisitions and other corporate transactions.

Our business is called "Harbourline Capital Advisors"
Our current website is www.harbourlinecap.com.au

I'd like to see a complete re-design of the site. (I'm happy to keep any of the existing images - but equally happy to scrap them completely and "start again".)

My preference is that the logo remain as it is. However, I would be very open to a re-colouring of the logo if it works better with a new webiste design.

The content of the website will remain the same. I'd like one additional section - "News" - which will allow us to manually post news items and which will pull in news feeds from current and past clients.

In terms of positioning / look-and-feel:

Our clients fall into two categories. I'd like the website to appeal to both:

1. The first category is: Executives from established technology or life-science companies (private or public), who engage us to assist with strategy, capital raising, corporate transactions.

2. The second category is: Entrepreneurs looking for advice in accessing angel funding or venture capital. The site should appeal to young tech-savvy entrepreneurs who are looking to engage a firm to provide such assistance.

To accomodate both target groups, the overriding feel should be one of professionalism, stability, trust and expertise. However, while the site should look fairly "corporate", I'd like it to feel contemporary and have an element of creativity and flair, reflecting the fact that our clients are often early-stage, innovative, technology companies. (I know this might be a tricky balance...)

Target Market(s)

Potential clients. Typically executives at technology or life-science companies or (more typically) entrepreneurs building their own companies

Industry/Entity Type

Business

Requirements
Must have
• 1. All content on the existing website
2. An additional section called "News" that allows us to easily add news items or articles and ideally which accepts news feeds from a handful of past and present clients
3. An ability to easily update and edit content
Should not have
• The site should not have "gimmicks". (Definitely no devices like the moving arrow in the current site!)

It should be fairly conservative, while still feeling contemporary and fresh.

```html
<!DOCTYPE html>
<html lang="en">
<head>
<meta charset="utf-8">
<title>Harbourline Capital Advisors</title>
<link href="https://fonts.googleapis.com/css2?family=Open+Sans:wght@400;600;700&family=Nunito+Sans:wght@400;600&display=swap" rel="stylesheet">
<style>
:root{
  --sky:#1fa9e1;
  --sky-light:#5cc8f0;
  --sky-deep:#0e86c6;
  --header-bg:#eaf5fb;
  --body-bg:#e2e2e2;
  --green:#8cc63f;
  --green-light:#bde57c;
  --green-dark:#5a8f14;
  --green-bar:#4f8a10;
  --ink:#1c1c1c;
  --text:#444;
  --muted:#888;
  --footer:#5a5a5a;
  --footer-dark:#4a4a4a;
  --white:#fff;
}
*{margin:0;padding:0;box-sizing:border-box}
html,body{width:971px;height:1200px;overflow:hidden}
body{position:relative;background:var(--body-bg);font-family:"Open Sans",Arial,sans-serif;color:var(--text)}
.abs{position:absolute}

.site-header{position:absolute;left:0;top:0;width:971px;height:90px;background:var(--header-bg)}
.brand{position:absolute;left:107px;top:19px;display:flex;align-items:center;gap:12px}
.brand-dot{width:55px;height:55px;border-radius:50%;background:var(--sky)}
.brand-name{font-family:"Nunito Sans",sans-serif;font-size:21px;color:#444;font-weight:400}
.call-bar{position:absolute;left:596px;top:8px;width:268px;height:21px;background:var(--green-bar);color:#fff;font-size:9.5px;line-height:21px;text-align:center}
.main-nav{position:absolute;left:452px;top:33px;display:flex;align-items:center;font-size:12.5px;color:#222}
.main-nav span{margin-right:26px}
.main-nav .is-active{background:linear-gradient(#5dcaf3,#1aa3dc);color:#fff;border-radius:14px;padding:6px 16px;margin-right:14px}
.main-nav .is-current{color:#5a9c1a}

.hero{position:absolute;left:0;top:90px;width:971px;height:354px;background:radial-gradient(circle at 55% 50%,#30c2f5,#119fdd 70%);}
.hero-figure{position:absolute;left:146px;top:-6px;width:284px;height:360px;border-radius:140px 140px 0 0;background:linear-gradient(#d9a26a,#c7c7c7 60%,#8f8f8f)}
.hero-arrow{position:absolute;top:160px}
.hero-copy{position:absolute;left:494px;top:60px;color:#fff;font-family:Arial,Helvetica,sans-serif;line-height:1}
.hero-copy .lead{font-size:18px}
.hero-copy .big{font-size:45px;letter-spacing:-1px;margin-top:14px}
.hero-copy .big small{font-size:16px;letter-spacing:0}
.hero-copy .big2{font-size:47px;letter-spacing:-1px;margin:6px 0 0 7px}
.hero-copy .sectors{font-size:14px;margin:2px 0 0 4px}
.hero-cta{position:absolute;left:500px;top:237px;width:209px;height:49px;border-radius:4px;background:linear-gradient(var(--green-light),var(--green));color:#2a3d0e;font-size:18px;text-align:center;line-height:49px;border:1px solid #7fb23a}
.hero-edge{position:absolute;left:0;top:444px;width:971px;height:7px;background:#fff}

.news-bar{position:absolute;left:107px;top:470px;width:757px;height:57px;background:linear-gradient(#fff,#ececec);border-radius:3px;box-shadow:0 2px 3px rgba(0,0,0,.15);display:flex;align-items:center}
.news-bar h2{font-weight:400;font-size:19px;color:#111;margin-left:39px;width:155px;font-family:Arial,sans-serif}
.news-bar p{font-size:11.5px;color:#444}
.news-dots{position:absolute;right:28px;top:24px;display:flex;gap:5px}
.news-dots i{width:10px;height:10px;border-radius:50%;background:#555;display:block}

.clients-card{position:absolute;left:107px;top:559px;width:498px;height:281px;background:#fff;border-radius:3px;box-shadow:0 1px 4px rgba(0,0,0,.2);overflow:hidden}
.clients-card h3{height:58px;background:linear-gradient(var(--sky-light),#3db8ea);color:#fff;font-weight:400;font-size:18.5px;line-height:58px;padding-left:27px}
.client{position:absolute;top:88px;width:200px;text-align:center;font-size:11px;line-height:13px;color:#333}
.client-icon{width:70px;height:60px;margin:0 auto 16px;background:#4a4a4a;border-radius:30px 30px 4px 4px}
.more-btn{display:block;width:150px;height:28px;margin:16px auto 0;background:linear-gradient(var(--green-light),var(--green));border:1px solid #7fb23a;border-radius:3px;line-height:26px;font-size:13px;color:#2a3d0e}

.what-we-do{position:absolute;left:107px;top:864px;width:500px}
.what-we-do h2{font-size:19px;color:#111;font-family:Arial,sans-serif}
.what-we-do p{font-size:11px;line-height:15px;color:#444;margin-top:6px}

.contact{position:absolute;left:637px;top:559px;width:237px;height:411px;background:linear-gradient(90deg,#d2d2d2,#e2e2e2 12%);padding:12px 0 0 22px}
.contact h2{font-size:19px;color:#111;font-family:Arial,sans-serif}
.contact h4{font-size:11.5px;font-weight:400;color:#222;display:flex;align-items:center;gap:6px;padding-bottom:9px;border-bottom:1px solid #c4c4c4;width:200px}
.contact .role{font-size:11px;color:#888;margin-top:12px}
.contact .mail{font-size:10.5px;color:#1d9ad6}
.map-block{width:55px;height:50px;background:linear-gradient(#8bc34a,#f0a030);border-radius:4px}
.addr{font-size:9.5px;color:#777;line-height:13px}
.social{display:flex;gap:28px;margin-top:0;font-size:18px;font-weight:700;color:#2a7bc0}

.site-footer{position:absolute;left:0;top:993px;width:971px;height:207px;background:radial-gradient(circle at 40% 10%,#6a6a6a,var(--footer-dark) 70%)}
.site-footer h2{position:absolute;left:105px;top:50px;font-size:19px;color:#2aa8e0;font-weight:400}
.footer-nav{position:absolute;left:105px;top:79px;font-size:10.5px;color:#ccc}
.footer-nav span{padding:0 6px;border-left:1px solid #888}
.footer-nav span:first-child{padding-left:0;border:0}
.footer-nav .is-current{color:#fff}
.footer-brand{position:absolute;left:637px;top:43px;display:flex;align-items:center;gap:10px;font-family:"Nunito Sans",sans-serif;font-size:14px;color:#3a3a3a}
.footer-brand i{width:42px;height:42px;border-radius:50%;background:#6f6f6f;display:block}
.footer-rule{position:absolute;left:105px;top:107px;width:760px;height:1px;background:#666}
.copyright{position:absolute;left:105px;top:117px;font-size:10px;color:#bbb}
.powered{position:absolute;right:106px;top:117px;font-size:10px;color:#bbb}
</style>
</head>
<body>

<header class="site-header">
  <div class="brand"><span class="brand-dot"></span><span class="brand-name">Harbourline Capital Advisors</span></div>
  <div class="call-bar">Call: +61 2 9000 1234 &nbsp;|&nbsp; Email: info@harbourlinecap.com.au</div>
  <nav class="main-nav">
    <span class="is-active">Home</span><span class="is-current">Our Services</span><span>Our Team</span><span>Our Experience</span><span style="margin:0">Contact Us</span>
  </nav>
</header>

<section class="hero">
  <div class="hero-figure" role="img" aria-label="Illustration of a friendly support advisor wearing a headset, gesturing toward the headline"></div>
  <svg class="hero-arrow" style="left:84px" width="24" height="34" viewBox="0 0 24 34"><path d="M20 3 6 17l14 14" fill="none" stroke="#fff" stroke-width="6"/></svg>
  <svg class="hero-arrow" style="left:866px" width="24" height="34" viewBox="0 0 24 34"><path d="M4 3l14 14L4 31" fill="none" stroke="#fff" stroke-width="6"/></svg>
  <div class="hero-copy">
    <div class="lead">Our focus is on the</div>
    <div class="big">TECHNOLOGY<small>AND</small></div>
    <div class="big2">LIFE-SCIENCE</div>
    <div class="sectors">SECTORS</div>
  </div>
  <div class="hero-cta">Get Our Services</div>
</section>
<div class="hero-edge"></div>

<section class="news-bar">
  <h2>Latest News</h2>
  <p>Entrepreneurs looking for advice in accessing angel funding or venture capital.</p>
  <div class="news-dots"><i></i><i></i></div>
</section>

<section class="clients-card">
  <h3>We Serve for Our Clients</h3>
  <div class="client" style="left:33px">
    <div class="client-icon" role="img" aria-label="Executive client icon"></div>
    Executives from established<br>technology or life-science<br>companies...
    <span class="more-btn">Get More Info</span>
  </div>
  <div class="client" style="left:272px">
    <div class="client-icon" role="img" aria-label="Entrepreneur client icon"></div>
    Entrepreneurs looking for advice<br>in accessing angel funding or<br>venture capital.
    <span class="more-btn">Get More Info</span>
  </div>
</section>

<section class="what-we-do">
  <h2>What We Do...</h2>
  <p>A corporate advisory firm with a focus on life-science and technology<br>Harbourline Capital Advisors is a specialist corporate advisory and investment firm with a focus on<br>high growth companies in the Australian life-science and technology sectors.</p>
</section>

<aside class="contact">
  <h2>Contact Details:</h2>
  <h4 style="margin-top:14px"><svg width="11" height="9" viewBox="0 0 11 9"><rect x=".5" y=".5" width="10" height="8" fill="none" stroke="#222"/><path d="M.5.5l5 4 5-4" fill="none" stroke="#222"/></svg>E-mail</h4>
  <p class="role">HCA - Managing Director</p>
  <p class="mail">info@harbourlinecap.com.au</p>
  <p class="role">HCA - Marketing Manager</p>
  <p class="mail">support@harbourlinecap.com.au</p>
  <h4 style="margin-top:40px"><svg width="9" height="12" viewBox="0 0 9 12"><path d="M4.5 0A4.5 4.5 0 0 0 0 4.5C0 8 4.5 12 4.5 12S9 8 9 4.5A4.5 4.5 0 0 0 4.5 0z" fill="#222"/><circle cx="4.5" cy="4.5" r="1.6" fill="#e2e2e2"/></svg>Location</h4>
  <div style="display:flex;gap:12px;margin-top:10px;align-items:flex-start">
    <div class="map-block" role="img" aria-label="Map marker icon"></div>
    <div class="addr">Level 2, 14 Quayline Street<br>Pyrmont NSW 2009<br>Australia</div>
  </div>
  <h4 style="margin-top:28px;width:183px"><svg width="9" height="9" viewBox="0 0 9 9"><path d="M4.5 0v9M0 4.5h9" stroke="#222" stroke-width="2"/></svg>Social Media</h4>
  <div class="social" style="margin-top:16px;margin-left:-4px"><span>Linkwave</span><span>Chirpline</span></div>
</aside>

<footer class="site-footer">
  <h2>What We Do...</h2>
  <div class="footer-nav"><span>Home</span><span>Our Services</span><span class="is-current">Our Team</span><span>Our Experience</span><span>Contact Us</span></div>
  <div class="footer-brand"><i></i>Harbourline Capital Advisors</div>
  <div class="footer-rule"></div>
  <div class="copyright">All Right Reserved Copyright © 2012 - Harbourline Capital Advisors</div>
  <div class="powered">Powered By : Northgrid Studio</div>
</footer>

</body>
</html>
```